Book on emotional dysfunction needs a book cover

This book, entitled "Inner Turmoil and the Scented Memory Path", by Darren Holloway, needs a front cover. The cover could possibly show an adult who is really a child, or a person actively smelling who not really there, like in an alternate dimension.

```html
<!DOCTYPE html>
<html lang="en">
<head>
<meta charset="utf-8">
<title>Inner Turmoil and the Scented Memory Path — Darren Holloway</title>
<link rel="stylesheet" href="https://fonts.googleapis.com/css2?family=Crimson+Pro:wght@400&family=Montserrat:wght@700&display=swap">
<style>
  :root {
    --ink-black: #05060a;
    --deep-purple: #3a2a7a;
    --electric-blue: #0aa6d8;
    --teal: #1b6f8c;
    --skin-orange: #c8642c;
    --skin-light: #e8b58e;
    --title-white: #ffffff;
    --author-yellow: #f6ea14;
  }
  html, body {
    margin: 0;
    padding: 0;
    width: 824px;
    height: 1200px;
    overflow: hidden;
    background: var(--ink-black);
  }
  .cover {
    position: relative;
    width: 824px;
    height: 1200px;
    overflow: hidden;
    background: var(--ink-black);
  }
  .cover-art {
    position: absolute;
    inset: 0;
    background:
      radial-gradient(ellipse 22% 14% at 52% 42%, var(--skin-light) 0%, rgba(200,100,44,0.0) 100%),
      radial-gradient(ellipse 30% 42% at 51% 58%, var(--skin-orange) 0%, rgba(140,90,60,0.7) 45%, rgba(0,0,0,0) 80%),
      radial-gradient(ellipse 70% 45% at 50% 55%, var(--electric-blue) 0%, var(--teal) 45%, rgba(10,20,40,0) 85%),
      radial-gradient(ellipse 90% 60% at 50% 55%, var(--deep-purple) 0%, rgba(20,15,40,0.6) 60%, var(--ink-black) 100%),
      linear-gradient(180deg, var(--ink-black) 0%, #0c1420 25%, #101a2a 60%, var(--ink-black) 100%);
  }
  .title {
    position: absolute;
    inset: 0;
    margin: 0;
    font-family: "Crimson Pro", "Times New Roman", serif;
    font-weight: 400;
    color: var(--title-white);
  }
  .title-line {
    position: absolute;
    left: 0;
    right: 0;
    text-align: center;
    line-height: 1;
    white-space: nowrap;
    font-size: 136px;
    letter-spacing: -1px;
  }
  .line-1 { top: 84px; }
  .line-2 { top: 238px; }
  .line-3 { top: 548px; }
  .line-4 { top: 705px; }
  .line-5 { top: 872px; font-size: 118px; }
  .author {
    position: absolute;
    left: 0;
    right: 0;
    top: 1076px;
    margin: 0;
    text-align: center;
    font-family: "Montserrat", "Arial", sans-serif;
    font-weight: 700;
    font-size: 36px;
    letter-spacing: 6px;
    text-transform: uppercase;
    color: var(--author-yellow);
    line-height: 1;
  }
</style>
</head>
<body>
  <main class="cover">
    <div class="cover-art" role="img" aria-label="Close-up of a person's nose and lips in orange light, fading into blue and purple, breaking apart into scattered dark triangular fragments"></div>
    <h1 class="title">
      <span class="title-line line-1">Inner</span>
      <span class="title-line line-2">Turmoil</span>
      <span class="title-line line-3">and the</span>
      <span class="title-line line-4">Scented</span>
      <span class="title-line line-5">Memory Path</span>
    </h1>
    <p class="author">Darren Holloway</p>
  </main>
</body>
</html>
```